Pet Spa Brochure

We are currently rebranding our Pet Resort & Spa. We have already completed our new website (www.tlmanimalhaven.com), business cards and logo (attached). We are currently working on our brochures and decided to take a different route in finishing them.

We are looking for a spa/massage, floral, oriental, relaxing, feminine and elegant design for the brochure specific to our Pet Spa services. We want professional and elegant but also original and unique if possible.

We mainly have dog customers but we also have cat customers so a picture of at least one cat would be perfect. Our Pet Resort (not Spa, just Resort) brochure can be found at www.tlmanimalhaven.com/rates and is the first two links listed. If things work well for our Pet Spa brochure we will be going back to redo the Pet Resort brochure as well.

I'm uploading a psd of the current brochure design so that you have access to the content. I can adjust the files later to make everything (or anything new) fit but please take the amount of text (present and future) into account when doing the design. I'm also uploading the psd of our current logo so it can be incorporated into the brochure as well.

The final design should communicate elegance, relaxation, pampering and happiness.
Updates

I'm attaching some of our pictures with pets in our pool, as well as some photos I saw on pixaroundly that show dogs being pampered/rubbed/massaged. The links to the photos are below. I'll be uploading the others to the project attachment area.

Target Market(s)

Women between the ages of 25 and 55

Industry/Entity Type

Business

Requirements
Must have
• Animals, paw prints, our logo, floral, oriental hot springs/spa feel.
Should not have
• Cartoon animals or cartoon like clipart.

```html
<!DOCTYPE html>
<html lang="en">
<head>
<meta charset="utf-8">
<title>TLM Animal Haven – Pet Spa Services</title>
<link rel="stylesheet" href="https://fonts.googleapis.com/css2?family=Courgette&family=Kurale&display=swap">
<style>
  :root {
    --paper: #f5efe9;
    --ink: #2c2220;
    --rose: #c8125f;
    --plum: #a3166f;
    --blossom: #f2c9d8;
    --blossom-soft: #f7dde6;
    --bark: #cdb6a8;
    --paw: #6b3a1f;
    --frame-grey: #5a5a5a;
  }
  * { box-sizing: border-box; margin: 0; padding: 0; }
  html, body { width: 1200px; height: 927px; overflow: hidden; background: var(--paper); }
  .brochure {
    position: relative; width: 1200px; height: 927px; overflow: hidden;
    background: var(--paper); color: var(--ink);
    font-family: "Kurale", serif; font-size: 13px;
  }
  .decor { position: absolute; }
  .blossom-branch {
    right: 0; top: 40px; width: 560px; height: 880px;
    background:
      radial-gradient(ellipse 90px 110px at 520px 120px, var(--blossom) 0%, transparent 70%),
      radial-gradient(ellipse 140px 90px at 320px 210px, var(--blossom-soft) 0%, transparent 70%),
      radial-gradient(ellipse 120px 100px at 460px 360px, var(--blossom) 0%, transparent 72%),
      radial-gradient(ellipse 110px 80px at 120px 380px, var(--blossom-soft) 0%, transparent 70%),
      radial-gradient(ellipse 120px 140px at 500px 620px, var(--blossom-soft) 0%, transparent 70%),
      radial-gradient(ellipse 100px 100px at 520px 820px, var(--blossom) 0%, transparent 70%);
    opacity: .85;
  }
  .pink-tree {
    left: 300px; top: 680px; width: 320px; height: 247px;
    background: radial-gradient(ellipse 150px 110px at 150px 80px, var(--blossom) 0%, rgba(242,201,216,.4) 55%, transparent 75%);
  }
  .tree-trunk { left: 370px; top: 860px; width: 90px; height: 67px; background: linear-gradient(var(--bark), #bda596); border-radius: 40px 40px 0 0; opacity: .8; }

  .column { position: absolute; }
  .col-left { left: 39px; top: 0; width: 318px; }
  .col-mid { left: 445px; top: 45px; width: 310px; }
  .col-right { left: 842px; top: 45px; width: 308px; }

  .brand {
    position: absolute; left: 100px; top: 120px; width: 200px;
    display: flex; align-items: center; gap: 10px;
    font-size: 24px; color: var(--rose); line-height: 1.1;
  }
  .brand-dot { width: 26px; height: 26px; border-radius: 50%; background: var(--rose); flex: none; }

  .section-title {
    font-family: "Courgette", cursive; color: var(--rose);
    font-size: 22px; text-align: center; line-height: 30px; font-weight: 400;
  }
  .col-left .section-title { position: absolute; top: 258px; left: 0; width: 318px; }
  .col-mid .section-title, .col-right .section-title { margin-bottom: 23px; }

  .price-list { list-style: none; }
  .item { margin-bottom: 15px; }
  .row { display: flex; align-items: baseline; line-height: 22px; white-space: nowrap; }
  .dots { flex: 1; border-bottom: 1.5px dotted var(--ink); margin: 0 3px; transform: translateY(-4px); }
  .tiers { display: grid; grid-template-columns: 133px 1fr; line-height: 22px; }
  .footnote { margin-top: 22px; line-height: 22px; }

  .feline-list { position: absolute; top: 311px; left: 0; width: 318px; }
  .feline-list .item { margin-bottom: 22px; }

  .photo { position: absolute; }
  .photo-paw-hold {
    left: 35px; top: 667px; width: 268px; height: 217px;
    border: 7px solid var(--plum); border-radius: 14px;
    background: linear-gradient(135deg, #b7772f, #d9a05a 50%, #8d5a26);
  }
  .photo-cat {
    left: 178px; top: 530px; width: 186px; height: 186px; border-radius: 50%;
    border: 7px solid var(--frame-grey);
    background: radial-gradient(circle at 40% 45%, #9c9284, #6f6a5e 60%, #c9c1a4);
  }
  .photo-dog-massage {
    left: 853px; top: 708px; width: 304px; height: 203px;
    border: 7px solid var(--plum); border-radius: 14px;
    background: linear-gradient(180deg, #f4f4f4 0%, #f1f1f1 40%, #d9b884 60%, #e9e9e9 100%);
  }
  .paw { position: absolute; width: 52px; height: 52px; fill: var(--paw); }
</style>
</head>
<body>
<main class="brochure">
  <div class="decor blossom-branch" role="img" aria-label="Cherry blossom branch with pink flowers"></div>
  <div class="decor pink-tree" role="img" aria-label="Soft pink flowering tree silhouette"></div>
  <div class="decor tree-trunk" role="img" aria-label="Tree trunk"></div>

  <section class="column col-left">
    <div class="brand"><span class="brand-dot"></span><span>TLM Animal Haven</span></div>

    <h2 class="section-title">Feline Spa Services</h2>
    <ul class="price-list feline-list">
      <li class="item"><div class="row">Bath<span class="dots"></span>$25</div></li>
      <li class="item"><div class="row">Bath &amp; Nails<span class="dots"></span>$30</div></li>
      <li class="item"><div class="row">Flea Bath<span class="dots"></span>$30</div></li>
      <li class="item"><div class="row">Nails Only<span class="dots"></span>$10</div></li>
      <li class="item"><div class="row">Brushout/Dematting<span class="dots"></span>$40/hr + Bath</div></li>
    </ul>
  </section>

  <svg class="paw" style="left:66px;top:540px" viewBox="0 0 52 52" aria-hidden="true">
    <ellipse cx="26" cy="36" rx="13" ry="11"/><ellipse cx="9" cy="22" rx="5" ry="7"/><ellipse cx="19" cy="12" rx="5" ry="7"/><ellipse cx="33" cy="12" rx="5" ry="7"/><ellipse cx="43" cy="22" rx="5" ry="7"/>
  </svg>
  <svg class="paw" style="left:48px;top:598px" viewBox="0 0 52 52" aria-hidden="true">
    <ellipse cx="26" cy="36" rx="13" ry="11"/><ellipse cx="9" cy="22" rx="5" ry="7"/><ellipse cx="19" cy="12" rx="5" ry="7"/><ellipse cx="33" cy="12" rx="5" ry="7"/><ellipse cx="43" cy="22" rx="5" ry="7"/>
  </svg>

  <div class="photo photo-paw-hold" role="img" aria-label="Photo of hands gently holding a golden dog's paw"></div>
  <div class="photo photo-cat" role="img" aria-label="Photo of a tabby cat nuzzling its owner"></div>

  <section class="column col-mid">
    <h2 class="section-title">Canine Spa Services</h2>
    <ul class="price-list">
      <li class="item">
        <div class="row">Bath<span class="dots"></span>See Below</div>
        <div class="tiers"><span>Under 20 lbs</span><span>$20</span><span>81–110 lbs</span><span>$35</span><span>21–50 lbs</span><span>$25</span><span>51–80 lbs</span><span>$30</span><span>111 lbs &amp; Over</span><span>$40</span></div>
      </li>
      <li class="item">
        <div class="row">Bath &amp; Nails<span class="dots"></span>See Below</div>
        <div class="tiers"><span>Under 20 lbs</span><span>$25</span><span>81–110 lbs</span><span>$40</span><span>21–50 lbs</span><span>$30</span><span>51–80 lbs</span><span>$35</span><span>111 lbs &amp; Over</span><span>$45</span></div>
      </li>
      <li class="item"><div class="row">Nails Only<span class="dots"></span>$10</div></li>
      <li class="item"><div class="row">Brushout/Dematting<span class="dots"></span>$40/hr + Bath</div></li>
      <li class="item">
        <div class="row">Professional Grooming*<span class="dots"></span>See Below</div>
        <div class="tiers"><span>Under 20lbs</span><span>At Least $40</span><span>21–50 lbs</span><span>At Least $50</span><span>51–80 lbs</span><span>At Least $60</span><span>81–110 lbs</span><span>At Least $70</span><span>111 lbs &amp; Over</span><span>At Least $80</span></div>
      </li>
      <li class="item"><div class="row">Shedless Program*<span class="dots"></span>$60 to $115</div></li>
      <li class="item"><div class="row">Flea Bath<span class="dots"></span>$3 to $10 + Bath</div></li>
      <li class="item"><div class="row">Special Bath<span class="dots"></span>$3 to $10 + Bath</div></li>
      <li class="item"><div class="row">Long Coats<span class="dots"></span>Extra Charge</div></li>
    </ul>
    <p class="footnote">*Includes the price of a Bath in the rate.</p>
  </section>

  <section class="column col-right">
    <h2 class="section-title">Canine Spa Extras</h2>
    <ul class="price-list">
      <li class="item" style="margin-bottom:22px"><div class="row">Anal Glands<span class="dots"></span>$??</div></li>
      <li class="item"><div class="row">Scent of the Month<span class="dots"></span>$5 + Bath</div></li>
      <li class="item"><div class="row">Bows/Bandannas<span class="dots"></span>$??</div></li>
      <li class="item"><div class="row">Creative Grooming<span class="dots"></span>$??</div></li>
      <li class="item"><div class="row">Whitening Treatment<span class="dots"></span>$??</div></li>
      <li class="item"><div class="row">Teeth Brushing<span class="dots"></span>$??</div></li>
      <li class="item">
        <div class="row">Temporary Airbrush Tattoos<span class="dots"></span>See Below</div>
        <div class="tiers"><span>Under 20lbs</span><span>At Least $40</span><span>21–50 lbs</span><span>At Least $50</span><span>51–80 lbs</span><span>At Least $60</span><span>81–110 lbs</span><span>At Least $70</span><span>111 lbs &amp; Over</span><span>At Least $80</span></div>
      </li>
      <li class="item"><div class="row">Nail Polish<span class="dots"></span>$60 to $115</div></li>
      <li class="item"><div class="row">Hot Towel Massage<span class="dots"></span>$10</div></li>
      <li class="item"><div class="row">Hot Spring Session<span class="dots"></span>$20</div></li>
      <li class="item"><div class="row">Hot Spring &amp; Towel Massage<span class="dots"></span>$25</div></li>
      <li class="item"><div class="row">Playtime<span class="dots"></span>$7</div></li>
      <li class="item"><div class="row">Downtime<span class="dots"></span>$10</div></li>
    </ul>
  </section>

  <svg class="paw" style="left:826px;top:698px" viewBox="0 0 52 52" aria-hidden="true">
    <ellipse cx="26" cy="36" rx="13" ry="11"/><ellipse cx="9" cy="22" rx="5" ry="7"/><ellipse cx="19" cy="12" rx="5" ry="7"/><ellipse cx="33" cy="12" rx="5" ry="7"/><ellipse cx="43" cy="22" rx="5" ry="7"/>
  </svg>
  <div class="photo photo-dog-massage" role="img" aria-label="Photo of a relaxed yellow Labrador receiving a massage"></div>
</main>
</body>
</html>
```